We are a music company that specializes in Music Mixing and Mastering. We also do vocal recording and create instrumentals for various artists. Our website is 738kv.com

Target Market(s)

Musicians, Record labels, rappers, and singers

Industry/Entity Type

Artists

Contact Information for Business Card

738KV
Industry Standard Mixing & Mastering
(555) 214-3907
sales@738kv.com
738kv.com

Requirements
Must have
• contact info and twitter (@738KV)

```html
<!DOCTYPE html>
<html lang="en">
<head>
<meta charset="utf-8">
<title>738KV Business Cards</title>
<link rel="stylesheet" href="https://fonts.googleapis.com/css2?family=Mulish:wght@400;700;900&display=swap">
<style>
  :root {
    --stage: #e6e4e1;
    --card-light: #ffffff;
    --card-dark: #2a2a2a;
    --ink: #1a1a1a;
    --ink-soft: #333333;
    --pattern-light-a: #f7f7f7;
    --pattern-light-b: #ffffff;
    --pattern-dark-a: #3a3a3a;
    --pattern-dark-b: #2c2c2c;
    --logo-light: #ffffff;
  }
  * { box-sizing: border-box; margin: 0; padding: 0; }
  html, body {
    width: 1200px; height: 1000px; overflow: hidden;
    background: var(--stage);
    font-family: "Mulish", Arial, sans-serif;
  }
  .card {
    position: absolute;
    overflow: hidden;
    box-shadow: 0 6px 18px rgba(0,0,0,0.25);
  }
  .card--front {
    left: 80px; top: 75px; width: 770px; height: 470px;
    background: var(--card-light);
    color: var(--ink);
  }
  .card--back {
    left: 335px; top: 442px; width: 805px; height: 478px;
    background: var(--card-dark);
  }
  .pattern { position: absolute; }
  .card--front .pattern {
    right: 0; top: 20px; width: 560px; height: 400px;
    background: linear-gradient(90deg, var(--pattern-light-b), var(--pattern-light-a) 40%, var(--pattern-light-a));
  }
  .card--back .pattern {
    left: 0; top: 20px; width: 100%; height: 440px;
    background: linear-gradient(180deg, var(--pattern-dark-a), var(--pattern-dark-b));
  }
  .front-logo {
    position: absolute; left: 38px; top: 228px;
    font-size: 66px; font-weight: 900; letter-spacing: -2px;
    color: var(--ink); line-height: 1;
  }
  .tagline {
    position: absolute; left: 38px; top: 334px;
    font-size: 18px; font-weight: 700; color: var(--ink);
    line-height: 22px;
  }
  .contact-list {
    position: absolute; left: 38px; top: 362px;
    list-style: none;
  }
  .contact-list li {
    display: flex; align-items: center; gap: 14px;
    height: 23px; font-size: 16px; color: var(--ink-soft);
  }
  .contact-list svg { width: 20px; height: 18px; fill: var(--ink); }
  .back-logo {
    position: absolute; left: 40px; top: 140px;
    font-size: 240px; font-weight: 900; letter-spacing: -8px;
    color: var(--logo-light); line-height: 1;
  }
</style>
</head>
<body>
  <section class="card card--front">
    <div class="pattern" role="img" aria-label="Faint repeating wordmark pattern"></div>
    <div class="front-logo">738KV</div>
    <p class="tagline">Industry Standard Mixing &amp; Mastering</p>
    <ul class="contact-list">
      <li>
        <svg viewBox="0 0 20 18" aria-hidden="true"><path d="M2 5c0-2 3-3 8-3s8 1 8 3v2h-4V5H6v2H2z"/><rect x="4" y="8" width="12" height="8" rx="1"/></svg>
        <span>(555) 214-3907</span>
      </li>
      <li>
        <svg viewBox="0 0 20 18" aria-hidden="true"><rect x="2" y="3" width="16" height="12"/><path d="M2 3l8 7 8-7" fill="none" stroke="#fff" stroke-width="1.6"/></svg>
        <span>sales@738kv.com</span>
      </li>
      <li>
        <svg viewBox="0 0 20 18" aria-hidden="true"><circle cx="10" cy="9" r="7"/><path d="M3 9h14M10 2c-3 4-3 10 0 14M10 2c3 4 3 10 0 14" fill="none" stroke="#fff" stroke-width="1.2"/></svg>
        <span>738kv.com</span>
      </li>
      <li>
        <svg viewBox="0 0 20 18" aria-hidden="true"><circle cx="10" cy="9" r="6"/></svg>
        <span>@738KV</span>
      </li>
    </ul>
  </section>

  <section class="card card--back">
    <div class="pattern" role="img" aria-label="Repeating grey wordmark pattern"></div>
    <div class="back-logo">738KV</div>
  </section>
</body>
</html>
```